New Innovative Product needs a new business card design

We need a business card design for a new product line based in Michigan called "Lendwise Tailwind." We are a credit company by nature however this product should have a clean, simple, "zorvik-esque" feel. We have a few tag lines we use that could or could not be used...."All Referral Roads Lead to You" we use the attached pic in much or our marketing and also use both a white and/or black logo. Also attached.

We want the image attached on the card in some form or another- the grass/sky image.

Reason: We are extending to go over options with management- (expiring on weekend)

Reason: To finalize our design pick. We will be in touch with the designer of choice within the next day or so...the last few entries have been great- Sorry for the delay.

Reason: Working with a couple different designs trying to get finalized

Reason: Final in the workds

Marketing

• We want the image attached on the card in some form or another- the grass/sky image.

```html
<!DOCTYPE html>
<html lang="en">
<head>
<meta charset="utf-8">
<title>Lendwise Tailwind – Business Card</title>
<link rel="stylesheet" href="https://fonts.googleapis.com/css2?family=Arimo:wght@700&family=Open+Sans:wght@400&family=Oxanium:wght@400;600;700&display=swap">
<style>
  :root {
    --backdrop: #ececec;
    --card-white: #ffffff;
    --sky-deep: #1f4fa8;
    --sky-light: #6f9ed8;
    --cloud: #e9eef5;
    --grass: #5fa52c;
    --grass-dark: #3f7d1c;
    --brand-green: #1f8a3e;
    --ink: #111111;
    --on-photo: #ffffff;
  }
  * { box-sizing: border-box; margin: 0; padding: 0; }
  html, body { width: 1200px; height: 1000px; overflow: hidden; }
  body { background: var(--backdrop); position: relative; }

  .card {
    position: absolute;
    top: 262px;
    width: 265px;
    height: 478px;
    overflow: hidden;
  }
  .card--front {
    left: 305px;
    border-radius: 0 14px 0 14px;
  }
  .card--back {
    left: 630px;
    background: var(--card-white);
    border-radius: 14px 0 14px 0;
  }

  .landscape {
    position: absolute;
    inset: 0;
    background:
      linear-gradient(to bottom,
        var(--sky-deep) 0%,
        #2a5cb4 35%,
        var(--sky-light) 62%,
        var(--cloud) 80%,
        var(--grass) 82%,
        var(--grass-dark) 100%);
  }

  .tagline {
    position: absolute;
    left: 20px;
    top: 122px;
    font-family: "Arimo", sans-serif;
    font-weight: 700;
    font-size: 35px;
    line-height: 33px;
    color: var(--on-photo);
    text-transform: uppercase;
  }

  .legal {
    position: absolute;
    left: 20px;
    top: 409px;
    font-family: "Open Sans", sans-serif;
    font-size: 12px;
    line-height: 16px;
    color: var(--on-photo);
  }

  .brand {
    position: absolute;
    left: 30px;
    top: 92px;
    display: flex;
    align-items: center;
    gap: 10px;
  }
  .brand__mark {
    width: 18px;
    height: 18px;
    background: var(--brand-green);
  }
  .brand__name {
    font-family: "Oxanium", sans-serif;
    font-weight: 600;
    font-size: 21px;
    color: var(--ink);
  }

  .contact {
    position: absolute;
    left: 24px;
    top: 312px;
    font-family: "Oxanium", sans-serif;
    color: var(--ink);
  }
  .contact__name {
    font-weight: 700;
    font-size: 16px;
    color: var(--brand-green);
    letter-spacing: 0.3px;
  }
  .contact__role {
    font-size: 11px;
    margin-top: 1px;
  }
  .contact__details {
    margin-top: 22px;
    font-size: 13px;
    line-height: 18px;
    font-style: normal;
  }
  .contact__label { color: var(--brand-green); }
</style>
</head>
<body>
  <section class="card card--front">
    <div class="landscape" role="img" aria-label="Photo of a blue sky with white clouds above a green field with a tractor track leading to the horizon"></div>
    <h1 class="tagline">All<br>Referral<br>Roads<br>Lead<br>To You</h1>
    <p class="legal">A Division of Meridian Ledger Group, Inc.®<br>All rights reserved</p>
  </section>

  <section class="card card--back">
    <div class="brand">
      <span class="brand__mark"></span>
      <span class="brand__name">Lendwise Tailwind</span>
    </div>
    <div class="contact">
      <p class="contact__name">Calder Voss</p>
      <p class="contact__role">Product Manager</p>
      <address class="contact__details">
        72903 W. Placeholder Rd.<br>
        Lakeside, MI 49999<br>
        <span class="contact__label">P:</span> 555.010.2468<br>
        <span class="contact__label">E:</span>cvoss@meridianledger.com
      </address>
    </div>
  </section>
</body>
</html>
```